Quietly Rooted Cover Design

Open to creative ideas, we don't have a set cover style in mind so have fun with it!
Front Cover for Ebook-Vendora and lumora shelf. Book title is "Quietly Rooted" sub title is "A Gentle Map of Heritage Meals", Author is Colette R Banfield. Website is www.thekeenherbalist.com.
Open to creative ideas, we dont' have a set cover style in mind so have fun with it!
We have attached some pictures of Colette which could be incorporated into the title. We can send you high def files if you need.
We have attached two book covers which we like to get you started, but feel free to have fun, we're looking for something creative and catchy

```html
<!DOCTYPE html>
<html lang="en">
<head>
<meta charset="utf-8">
<title>Quietly Rooted – Cover Set</title>
<link href="https://fonts.googleapis.com/css2?family=Lato:wght@700&family=Lora:wght@400&family=Noto+Serif:wght@700&display=swap" rel="stylesheet">
<style>
  :root {
    --backdrop: #5a4636;
    --gold-light: #fbe08a;
    --gold-mid: #f0b73a;
    --gold-deep: #d58d1c;
    --red: #c8191c;
    --red-dark: #8f1010;
    --ring: #e07a2a;
    --title-red: #b3261e;
    --ink: #111111;
    --white: #ffffff;
  }
  * { margin: 0; padding: 0; box-sizing: border-box; }
  html, body { width: 1200px; height: 784px; overflow: hidden; }
  body { background: var(--backdrop); position: relative; }

  .cover {
    position: absolute;
    width: 494px;
    height: 697px;
    top: 48px;
    background: radial-gradient(ellipse at 55% 40%, var(--gold-light) 0%, var(--gold-mid) 45%, var(--gold-deep) 100%);
    box-shadow: 0 4px 14px rgba(0,0,0,0.45);
    overflow: hidden;
  }
  .cover--front { left: 87px; }
  .cover--back { left: 623px; }
  .cover-art { position: absolute; inset: 0; width: 100%; height: 100%; }

  .front-title {
    position: absolute;
    left: 0; right: 0;
    top: 548px;
    text-align: center;
  }
  .front-title__main {
    font-family: "Lora", Georgia, serif;
    font-weight: 400;
    font-size: 31px;
    line-height: 36px;
    color: var(--title-red);
  }
  .front-title__series {
    font-family: "Lato", Arial, sans-serif;
    font-weight: 700;
    font-size: 25px;
    line-height: 32px;
    color: var(--ink);
  }

  .author-bio {
    position: absolute;
    left: 78px;
    width: 340px;
    top: 480px;
    font-family: "Noto Serif", Georgia, serif;
    font-weight: 700;
    font-size: 16.5px;
    line-height: 23px;
    color: var(--ink);
    text-align: justify;
    text-align-last: center;
    hyphens: manual;
  }
  .author-site {
    position: absolute;
    left: 0; right: 0;
    top: 652px;
    text-align: center;
    font-family: "Lato", Arial, sans-serif;
    font-weight: 700;
    font-size: 21px;
    color: var(--white);
  }
</style>
</head>
<body>

<section class="cover cover--front">
  <svg class="cover-art" viewBox="0 0 494 697" xmlns="http://www.w3.org/2000/svg">
    <path class="author-photo" role="img" aria-label="Portrait of the author leaning against a tree trunk on a city street"
          d="M0,38 Q260,18 494,178 L494,330 Q250,360 0,460 Z" fill="#c9c3bb"/>
    <path class="swoosh swoosh--top" d="M0,38 Q260,18 494,178" fill="none" stroke="var(--red)" stroke-width="9"/>
    <path class="swoosh swoosh--bottom" d="M0,462 Q250,362 494,332" fill="none" stroke="var(--red)" stroke-width="22"/>

    <g class="food-tile">
      <circle cx="78" cy="459" r="57" fill="var(--ring)"/>
      <circle cx="78" cy="459" r="50" fill="var(--white)"/>
      <circle role="img" aria-label="Photo of a hearty beef stew" cx="78" cy="459" r="47" fill="#6b3322"/>
    </g>
    <g class="food-tile">
      <circle cx="240" cy="442" r="65" fill="var(--ring)"/>
      <circle cx="240" cy="442" r="58" fill="var(--white)"/>
      <circle role="img" aria-label="Photo of grilled halloumi on a grain salad" cx="240" cy="442" r="55" fill="#c89a5c"/>
    </g>
    <g class="food-tile">
      <circle cx="403" cy="366" r="77" fill="var(--ring)"/>
      <circle cx="403" cy="366" r="70" fill="var(--white)"/>
      <circle role="img" aria-label="Photo of roasted vegetables with mushrooms" cx="403" cy="366" r="66" fill="#7a5a3e"/>
    </g>
  </svg>
  <div class="front-title">
    <p class="front-title__main">A Gentle Map<br>of Heritage Meals</p>
    <p class="front-title__series">Quietly Rooted</p>
  </div>
</section>

<section class="cover cover--back">
  <svg class="cover-art" viewBox="0 0 494 697" xmlns="http://www.w3.org/2000/svg">
    <g class="food-tile">
      <circle cx="139" cy="237" r="41" fill="var(--ring)"/>
      <circle cx="139" cy="237" r="36" fill="var(--white)"/>
      <circle role="img" aria-label="Photo of a baked slice" cx="139" cy="237" r="33" fill="#8a6a44"/>
    </g>
    <g class="food-tile">
      <circle cx="345" cy="232" r="41" fill="var(--ring)"/>
      <circle cx="345" cy="232" r="36" fill="var(--white)"/>
      <circle role="img" aria-label="Photo of a tomato based dish" cx="345" cy="232" r="33" fill="#b5532a"/>
    </g>
    <g class="food-tile">
      <circle cx="125" cy="357" r="58" fill="var(--ring)"/>
      <circle cx="125" cy="357" r="52" fill="var(--white)"/>
      <circle role="img" aria-label="Photo of chicken and greens" cx="125" cy="357" r="49" fill="#8c9a5a"/>
    </g>
    <g class="food-tile">
      <circle cx="360" cy="348" r="65" fill="var(--ring)"/>
      <circle cx="360" cy="348" r="59" fill="var(--white)"/>
      <circle role="img" aria-label="Photo of a golden crumb topped bake" cx="360" cy="348" r="56" fill="#d9b466"/>
    </g>
    <g class="food-tile">
      <circle cx="240" cy="412" r="53" fill="var(--ring)"/>
      <circle cx="240" cy="412" r="47" fill="var(--white)"/>
      <circle role="img" aria-label="Photo of a spinach and pumpkin salad" cx="240" cy="412" r="44" fill="#5f7a32"/>
    </g>
    <g class="food-tile">
      <circle cx="185" cy="384" r="37" fill="var(--ring)"/>
      <circle cx="185" cy="384" r="32" fill="var(--white)"/>
      <circle role="img" aria-label="Photo of a beetroot salad" cx="185" cy="384" r="29" fill="#8a3a4a"/>
    </g>
    <g class="food-tile">
      <circle cx="307" cy="375" r="37" fill="var(--ring)"/>
      <circle cx="307" cy="375" r="32" fill="var(--white)"/>
      <circle role="img" aria-label="Photo of roasted cauliflower" cx="307" cy="375" r="29" fill="#cdbf9a"/>
    </g>
    <g class="food-tile">
      <circle cx="243" cy="290" r="86" fill="var(--ring)"/>
      <circle cx="243" cy="290" r="79" fill="var(--white)"/>
      <circle role="img" aria-label="Photo of chocolate coconut slices" cx="243" cy="290" r="75" fill="#5a3a2a"/>
    </g>
  </svg>
  <p class="author-bio">Born in the south-east suburbs of Melbourne, Australia Nutritionist and Master Fitness Trainer, Colette Rae Banfield is passion-ate about living a life that she loves!</p>
  <p class="author-site">www.thekeenherbalist.com.</p>
</section>

</body>
</html>
```